Laundry Service Description Tri-Fold Brochure

My laundry business offers a service called "Velnora - Wet Cleaning"
I am after a design for a tri fold brochure to hand out to my customers. This will detail the benefits of wet cleaning vs dry cleaning.
I want the brochure to highlight the customer benefits NOT the business benefits.
I have attached the logo of our laundry which should be included
A couple of links here for more information and pdfs are attached:
https://brindlepartsupplyhub.com.au/laundry/velnora-wet-cleaning.html
https://www.quorv.co.za/wet-cleaning/
I have attached the design of our laundry window and ideally i want the brochure designed similar

```html
<!DOCTYPE html>
<html lang="en">
<head>
<meta charset="utf-8">
<title>Lumera Laundry Services – Brochure and Business Card</title>
<link href="https://fonts.googleapis.com/css2?family=Roboto:wght@400;500;700&family=Rubik:wght@500;700&display=swap" rel="stylesheet">
<style>
:root{
  --blue:#2f8fd6;
  --blue-deep:#1f76c0;
  --blue-light:#4aa8e2;
  --navy:#1d2a4a;
  --green:#7cc243;
  --ink:#2b2f36;
  --aqua:#9fe3f0;
  --paper:#ffffff;
  --stage:#ececec;
}
*{box-sizing:border-box;margin:0;padding:0}
html,body{width:1200px;height:2875px;overflow:hidden}
body{background:var(--stage);font-family:Roboto,Arial,sans-serif;color:var(--ink);position:relative}
.abs{position:absolute}
.panel{position:absolute;top:0;bottom:0;overflow:hidden}
.photo{position:absolute}
h2,.display{font-family:Rubik,Arial,sans-serif;font-weight:700;line-height:1}
.wave{position:absolute;left:0;bottom:0;width:100%;height:46px}

/* tick list */
.ticks{list-style:none}
.ticks li{position:relative;padding-left:20px}
.ticks li::before{content:"";position:absolute;left:0;top:2px;width:12px;height:12px;border-radius:50%;background:var(--blue)}
.ticks li::after{content:"";position:absolute;left:4px;top:4px;width:3px;height:6px;border:solid #fff;border-width:0 2px 2px 0;transform:rotate(45deg)}
.ticks.green li::before{background:var(--green)}

/* outside spread */
.outside{left:148px;top:125px;width:862px;height:630px;background:var(--paper);box-shadow:0 8px 24px rgba(0,0,0,.15)}
.safe-list h2{color:var(--blue);font-size:18px;line-height:20px}
.safe-list ul{margin-top:14px;font-size:12.5px;line-height:15px}
.safe-list li{margin-bottom:4px}
.footnote{font-size:7.5px;line-height:9px;color:#555}
.contact{background:linear-gradient(180deg,var(--blue-light),var(--blue-deep));color:#fff;text-align:center}
.contact .address{font-size:16px;line-height:19px}
.contact .label{font-size:13px;display:flex;align-items:center;justify-content:center;gap:6px}
.contact .label::before,.contact .label::after{content:"";width:48px;height:1px;background:#fff}
.phone{font-family:Rubik,Arial,sans-serif;font-weight:700;display:flex;align-items:center;gap:6px}
.phone .dot{width:18px;height:18px;border-radius:50%;background:currentColor;position:relative}
.phone svg{position:absolute;left:4px;top:4px}
.brand{font-family:Roboto,Arial,sans-serif;font-weight:500;color:var(--blue);display:flex;align-items:center;gap:8px}
.brand .mark{border-radius:50%;background:var(--blue)}
.join h2{font-family:Rubik,Arial,sans-serif;color:var(--navy);font-weight:500}
.pill{background:var(--blue);color:#fff;font-weight:700;border-radius:14px;text-align:center}

/* inside spread */
.inside{left:134px;top:937px;width:898px;height:648px;background:#e4f1fa;box-shadow:0 8px 24px rgba(0,0,0,.15)}
.soft-bg{background:linear-gradient(180deg,#f2f8fc,#d9ecf8)}
.what h2{color:var(--blue);font-size:20px}
.what .intro{font-size:17px;line-height:18px;color:var(--ink)}
.what ul{font-size:12.5px;line-height:15px;margin-top:20px}
.what li{margin-bottom:14px;border-left:1px solid #8ab;margin-left:6px;padding-left:14px}
.what li::before{left:-6px}
.what li::after{left:-2px}
.banner{background:var(--blue);color:#fff;border:2px solid #fff;border-radius:4px;font-family:Rubik,Arial,sans-serif;font-weight:700;font-size:21px;line-height:21px;padding:6px 10px}
.natural .big{color:var(--green);font-family:Rubik,Arial,sans-serif;font-weight:700;font-size:38px;line-height:36px}
.natural .sub{color:var(--blue);font-family:Rubik,Arial,sans-serif;font-weight:700;font-size:17px}
.natural ul{font-size:13px;line-height:15px}
.natural li{margin-bottom:8px}
.natural li b{color:var(--blue);font-weight:700;display:block}
.steps h2{color:var(--blue);font-size:19px;line-height:17px}
.steps .lead{font-size:16px;line-height:18px;color:#111}
.steps h3{color:var(--blue);font-size:14px;font-weight:700;margin-top:14px}
.steps p{font-size:10.5px;line-height:13px;margin-top:8px;color:#222}

/* business card */
.card{position:absolute;left:268px;width:699px;height:398px;border-radius:22px;overflow:hidden;box-shadow:0 14px 24px rgba(0,0,0,.22)}
.card.front{top:1880px;background:var(--paper)}
.card.back{top:2378px;background:linear-gradient(180deg,var(--blue),var(--blue-deep))}
.person{font-size:23px;font-weight:700;color:var(--blue)}
.role{font-size:16px;font-weight:500;color:#222}
.card .rule{height:1px;background:#444}
.card .lines{font-size:16px;line-height:20px;color:#333}
.card .lines li{list-style:none;padding-left:22px;position:relative}
.card .lines li::before{content:"";position:absolute;left:2px;top:5px;width:10px;height:10px;border-radius:50%;background:var(--blue)}
</style>
</head>
<body>

<!-- OUTSIDE SPREAD -->
<section class="outside abs" aria-label="Brochure outside">
  <div class="panel safe-list" style="left:0;width:283px;background:var(--paper)">
    <div class="photo" role="img" aria-label="Photo of a person loading clothes into a laundry machine" style="left:0;top:0;width:283px;height:195px;background:linear-gradient(135deg,#7f8a92,#c7cdd1 55%,#b98a6a)"></div>
    <h2 class="abs" style="left:33px;top:218px">WHATS SAFE TO<br>BE WET CLEANED?</h2>
    <ul class="ticks abs" style="left:33px;top:250px;width:240px">
      <li>Delicate fabrics* such<br>as handwoven or embroidered</li>
      <li>Items with glued sequins,<br>small beads &amp; embellishments</li>
      <li>Silk, hemp, flax, viscose and rayon</li>
      <li>Suit Trousers &amp; Jackets</li>
      <li>Wool/Cashmere</li>
      <li>Curtains, both lined &amp; non-lined</li>
      <li>Wedding Dresses*</li>
      <li>Outdoor Jackets and coats</li>
      <li>Puffer jackets with down fillings</li>
      <li>Shirts of any material</li>
      <li>Dresses and ball Gowns</li>
      <li>Fabric Shoes &amp; Trainers</li>
    </ul>
    <p class="footnote abs" style="left:31px;top:548px;width:225px">*A few items need extra care, such as heavy satin and older duchess satin. If in doubt, our team is happy to check your garments first.</p>
    <svg class="wave" viewBox="0 0 283 46" preserveAspectRatio="none"><path d="M0 20 C80 40 180 10 283 30 V46 H0Z" fill="var(--aqua)"/></svg>
  </div>

  <div class="panel contact" style="left:283px;width:297px">
    <div class="abs" role="img" aria-label="Illustration of floating soap bubbles" style="left:100px;top:42px;width:110px;height:140px;background:radial-gradient(circle at 50% 40%,rgba(255,255,255,.45),rgba(255,255,255,0) 65%)"></div>
    <p class="address abs" style="left:0;right:0;top:250px">Leoforos Akti Olympion<br>118 Larnaka, 6023</p>
    <p class="label abs" style="left:0;right:0;top:313px">BOOK SERVICES</p>
    <p class="phone abs" style="left:42px;top:330px;font-size:24px;color:#fff"><span class="dot" style="color:#fff"><svg width="10" height="10" viewBox="0 0 10 10"><path d="M2 1 L4 3 L3 4 Q4 6 6 7 L7 6 L9 8 L8 9 Q3 9 1 2Z" fill="var(--blue)"/></svg></span>+357 23 604 918</p>
    <p class="abs" style="left:0;right:0;top:360px;font-size:15px;font-weight:500">LUMERALAUNDRY.COM.CY</p>
    <p class="abs" style="left:0;right:0;top:402px;font-size:16px;font-weight:700">MON-SAT</p>
    <p class="abs" style="left:0;right:0;top:420px;font-size:15px">9:00 AM to 5:00 PM</p>
    <svg class="wave" viewBox="0 0 297 46" preserveAspectRatio="none"><path d="M0 26 C90 12 200 34 297 18 V46 H0Z" fill="var(--blue-deep)"/></svg>
  </div>

  <div class="panel join" style="left:580px;width:282px;background:var(--paper)">
    <div class="brand abs" style="left:48px;top:42px;font-size:36px"><span class="mark" style="width:14px;height:14px"></span>lumera</div>
    <p class="abs" style="left:62px;top:82px;font-size:15px;color:#555;letter-spacing:1px">Laundry Services</p>
    <div class="photo" role="img" aria-label="Photo of a smiling woman sitting beside a washing machine" style="left:0;top:120px;width:282px;height:190px;background:linear-gradient(90deg,#cfd8de,#f1f4f6 45%,#d5dde2)"></div>
    <h2 class="abs" style="left:40px;top:370px;font-size:22px">JOIN THE</h2>
    <p class="display abs" style="left:38px;top:394px;font-size:40px;color:var(--blue-light)">Velnora</p>
    <h2 class="abs" style="left:38px;top:437px;font-size:30px">REVOLUTION</h2>
    <ul class="ticks abs" style="left:42px;top:487px;font-size:12.5px;line-height:15px;width:200px">
      <li>No air or water pollution</li>
      <li>The process only uses water &amp;<br>Biodegradable Detergents</li>
    </ul>
    <p class="pill abs" style="left:30px;top:550px;width:210px;height:26px;line-height:26px;font-size:13px">LUMERALAUNDRY.COM.CY</p>
    <svg class="wave" viewBox="0 0 282 46" preserveAspectRatio="none"><path d="M0 30 C90 14 200 36 282 20 V46 H0Z" fill="var(--aqua)"/></svg>
  </div>
</section>

<!-- INSIDE SPREAD -->
<section class="inside abs" aria-label="Brochure inside">
  <div class="panel what soft-bg" style="left:0;width:298px">
    <h2 class="abs" style="left:39px;top:42px">WHAT IS VELNORA WASH?</h2>
    <p class="intro abs" style="left:39px;top:62px;width:250px">Velnora is an eco friendly<br>alternative to dry cleaning</p>
    <ul class="ticks abs" style="left:39px;top:104px;width:240px">
      <li>Wet cleaning uses only water &amp; bio degradable detergent rather than the carcinogenic solvents used in the traditional 'dry cleaning'</li>
      <li>Our process therefore results in a huge increase in efficiency &amp; quality and you get items back cleaner, fastyer and with significantly less impact on the environment</li>
      <li>To help limit any potential health risks, dry cleaners have been adviced to phase out dry cleaning machines that uses PERC</li>
    </ul>
    <p class="banner abs" style="left:37px;top:366px;width:225px">A BETTER CLEAN<br>IN A BETTER WAY</p>
    <div class="photo" role="img" aria-label="Photo of stacked folded towels beside a detergent bottle" style="left:20px;top:440px;width:240px;height:180px;border-radius:40% 40% 0 0;background:linear-gradient(180deg,#6fb6e6,#c9a9a0 50%,#9fb2c0)"></div>
    <svg class="wave" viewBox="0 0 298 46" preserveAspectRatio="none"><path d="M0 26 C90 40 200 14 298 30 V46 H0Z" fill="var(--aqua)"/></svg>
  </div>

  <div class="panel natural soft-bg" style="left:298px;width:300px">
    <div class="brand abs" style="left:38px;top:36px;font-size:40px"><span class="mark" style="width:15px;height:15px"></span>lumera</div>
    <p class="abs" style="left:52px;top:80px;font-size:16px;color:#555;letter-spacing:1px">Laundry Services</p>
    <p class="big abs" style="left:34px;top:104px">NATURAL</p>
    <p class="sub abs" style="left:34px;top:138px">AND SAFE CLEANING</p>
    <ul class="ticks green abs" style="left:33px;top:172px;width:250px">
      <li><b>Better cleaning Quality</b></li>
      <li><b>Safe for people</b>No adverse health affects on either operators or customers</li>
      <li><b>Safe for all garments</b>You can clean any garment with Velnora Deep Care that you would traditionally dry clean</li>
      <li><b>Compliant with any sustainable standards Ideal for cleaning special items.</b>E.g children's and baby clothing</li>
    </ul>
    <p class="label abs" style="left:0;right:0;top:415px;font-size:13px;color:#222;display:flex;align-items:center;justify-content:center;gap:6px"><span style="width:46px;height:1px;background:#222"></span>BOOK SERVICES<span style="width:46px;height:1px;background:#222"></span></p>
    <p class="phone abs" style="left:38px;top:432px;font-size:23px;color:var(--blue)"><span class="dot"><svg width="10" height="10" viewBox="0 0 10 10"><path d="M2 1 L4 3 L3 4 Q4 6 6 7 L7 6 L9 8 L8 9 Q3 9 1 2Z" fill="#fff"/></svg></span>+357 23 604 918</p>
    <div class="photo" role="img" aria-label="Photo of a laundry worker holding a basket of clothes" style="left:20px;top:475px;width:255px;height:173px;background:linear-gradient(180deg,#d7e6f0,#b88c6b 40%,#9cb8a8 75%,#c9b070)"></div>
  </div>

  <div class="panel steps soft-bg" style="left:598px;width:300px">
    <h2 class="abs" style="left:27px;top:27px">HOW DOES<br>WET CLEANING<br>LAUNDRY WORK?</h2>
    <div class="abs" style="left:27px;top:90px;width:245px">
      <p class="lead">Bring us your laundry<br>we do the rest! It's that simple.</p>
      <h3>Step1</h3>
      <p>Items are sorted into textile, colour, weight and soiling categories. Spotting stain removers are added for stains that may need a bit of extra help to remove e.g make-up. High pressure air and water with a vacuum pump are used to push and pull stains out of fabrics with minimal energy use.</p>
      <h3>Step2</h3>
      <p>Wet clean cycles are then selected that correspond with the material and treatment required. Most cycles are run at dynamic temperatures.</p>
      <h3>Step3</h3>
      <p>Our machines initially coat items in a layer of dirt-repelling molecules that prevent stains from re-depositing on the items during processing. A mixture of slow mechanical action, soaking and a shower pump inside the drum gently remove dirt and stains before a final rinse and conditioning.</p>
      <h3>Step4</h3>
      <p>The garments are then dried using specialised computer programs that analyse the water content of the garment dynamically. The temperature decreases as the cycle progresses to prevent shrinking. After items are dried they are finished by hand using a former that uses steam to remove all creases and relax the fibres into position.</p>
    </div>
    <svg class="wave" viewBox="0 0 300 46" preserveAspectRatio="none"><path d="M0 30 C90 16 200 38 300 22 V46 H0Z" fill="var(--aqua)"/></svg>
  </div>
</section>

<!-- BUSINESS CARD FRONT -->
<section class="card front" aria-label="Business card front">
  <div class="brand abs" style="left:398px;top:70px;font-size:56px"><span class="mark" style="width:20px;height:20px"></span>lumera</div>
  <p class="abs" style="left:418px;top:132px;font-size:22px;color:#555;letter-spacing:3px">Laundry Services</p>
  <p class="person abs" style="left:41px;top:238px">Daniel Evros</p>
  <p class="role abs" style="left:41px;top:266px">President</p>
  <div class="rule abs" style="left:41px;right:41px;top:292px"></div>
  <ul class="lines abs" style="left:41px;top:306px">
    <li>+357 23 604 918</li>
    <li>info@lumeralaundry.com.cy</li>
    <li>lumeralaundry.com.cy</li>
  </ul>
  <p class="lines abs" style="right:41px;top:298px;text-align:right">Leoforos<br>Akti Olympion<br>118 Larnaka, 6023</p>
</section>

<!-- BUSINESS CARD BACK -->
<section class="card back" aria-label="Business card back">
  <div class="abs" style="left:0;right:0;top:150px;display:flex;justify-content:center;align-items:center;gap:14px;font-family:Roboto,Arial,sans-serif;font-weight:500;font-size:80px;color:#fff"><span style="width:26px;height:26px;border-radius:50%;background:#fff"></span>lumera</div>
  <p class="abs" style="left:0;right:0;top:250px;text-align:center;font-size:30px;color:#fff;letter-spacing:5px">Laundry Services</p>
  <svg class="wave" style="height:80px" viewBox="0 0 699 80" preserveAspectRatio="none"><path d="M0 40 C200 10 450 60 699 30 V80 H0Z" fill="var(--blue-light)" opacity=".6"/><path d="M0 60 C220 40 470 75 699 55 V80 H0Z" fill="#5cc0ee" opacity=".6"/></svg>
</section>

</body>
</html>
```